Medical Breast Thermography Brochure Needed

Looking for a brochure that matches the theme and overall look/feel of our website brightoakcare.com.

http://brightoakcare.com/ourservices/breast-thermography/

I have previously used PixelVenue for logo, business card, and brochure and have been very happy, as soon as designs start being submitted I will switch to guaranteed payment.

I'm looking for a professional, clean, simple, minimalist, bold design.
Colors would ideally be greens and blues, or pink, cool tones, muted colors, or graytones.

See attached word document for content for brochure.

I would like to have the TH1-TH5 images in the Vantora thermo brochure 11.pdf document in the brochure.

Also would like one fold to compare mammogram with breast thermography like in BOCM_thermography_vs_mammography.jpg

I have attached a copy of our prior overall practice brochure to see what type of design I would like.

Feel free to use any stock photos.

```html
<!DOCTYPE html>
<html lang="en">
<head>
<meta charset="utf-8">
<title>Breast Thermography Brochure</title>
<link href="https://fonts.googleapis.com/css2?family=Roboto:wght@300;400;700&family=Roboto+Condensed:wght@300;400;700&display=swap" rel="stylesheet">
<style>
:root{
  --pink:#e23be6;
  --pink-light:#f4b5f6;
  --pink-pale:#f7c8f8;
  --magenta:#ff2cf5;
  --navy:#1f5e80;
  --blue:#2f7fb4;
  --sky:#4aa0e6;
  --green:#97c93c;
  --purple:#9a1fdc;
  --ink:#333;
  --grey:#8a8a8a;
}
*{box-sizing:border-box;margin:0;padding:0}
html,body{width:1200px;height:927px;overflow:hidden;background:#fff}
body{position:relative;font-family:"Roboto Condensed",Arial,sans-serif;color:var(--ink);font-size:8.3px;line-height:1.3}
.abs{position:absolute}
.pk{color:var(--pink);font-weight:700}
.bl{color:var(--blue)}
.nv{color:var(--navy);font-weight:700}
.bb{color:var(--blue);font-weight:700}
b{font-weight:700}
.display{font-family:"Roboto",Arial,sans-serif;line-height:1}

/* left column */
.facts{left:34px;top:13px;width:334px;list-style:none;line-height:10.8px}
.facts li{position:relative;padding-left:12px;margin-bottom:10.8px}
.facts li::before{content:"";position:absolute;left:0;top:1px;width:5px;height:9px;border-radius:50% 0 50% 0;background:linear-gradient(90deg,var(--green),var(--navy))}
.what-big{left:127px;top:288px;font-size:26px;font-weight:300;color:var(--navy)}
.what-sub{left:127px;top:311px;font-size:13px;font-weight:700;color:var(--pink)}
.what-q{left:258px;top:292px;font-size:38px;font-weight:300;color:var(--navy)}
.intro{left:37px;top:342px;width:331px;line-height:9.9px}
.intro p{margin-bottom:10.1px;text-align:justify}
.risk{left:38px;top:502px;width:218px;display:flex;align-items:center;justify-content:space-between;font-size:7px}
.risk .dot{width:6px;height:6px;border-radius:50%}
.thermo{top:517px;width:100px;height:85px}
.th-code{top:603px;font-size:12px;font-weight:700;color:var(--pink);line-height:1}
.th-cap{top:617px;font-size:8.8px;line-height:11px;color:var(--navy)}
.ben-big{left:265px;top:519px;font-size:26px;font-weight:300;color:var(--navy)}
.ben-sub{left:265px;top:541px;font-size:13px;font-weight:700;color:var(--pink);line-height:13px}
.ben-list{left:265px;top:572px;list-style:disc;padding-left:16px;font-size:8.3px;line-height:11.5px}
.diff{left:16px;top:742px;width:160px}
.diff div{font-family:"Roboto",Arial,sans-serif;line-height:.98}
.diff .l1{font-size:24px;font-weight:300;color:var(--navy)}
.diff .l2{font-size:19px;font-weight:700;color:var(--purple)}
.diff .l3{font-size:16px;font-weight:300;color:var(--navy);padding-left:58px}
.diff .l4{font-size:18px;font-weight:300;color:var(--pink);padding-left:17px}
.diff .amp{position:absolute;left:0;top:58px;font-family:"Roboto",Arial,sans-serif;font-size:40px;font-weight:300;color:var(--sky);line-height:1}
.diff .l5,.diff .l6{font-size:16.5px;font-weight:700;color:var(--pink);padding-left:30px}
.diff-text{left:177px;top:699px;width:209px;line-height:10.9px}
.diff-text p{margin-bottom:10.7px;text-align:justify}

/* middle column */
.who-title{left:504px;top:20px;font-size:28px;font-weight:300;color:var(--navy)}
.who-title strong{font-weight:700}
.who-sub{left:561px;top:45px;font-size:12.5px;font-weight:700;color:var(--pink)}
.who-q{left:697px;top:28px;font-size:40px;font-weight:300;color:var(--navy)}
.mid{left:436px;width:324px;text-align:center}
.who-list{top:68px;line-height:10px}
.who-list p{margin-bottom:9.7px}
.seven{left:572px;top:478px;font-size:92px;font-weight:700;color:#c9c9c9;font-style:italic;opacity:.7}
.addl-big{top:493px;font-size:26px;font-weight:300;color:var(--navy)}
.addl-sub{top:515px;font-size:19.5px;font-weight:700;color:var(--pink)}
.addl-vs{top:534px;font-size:14px;font-weight:300;color:var(--navy)}
.fact{line-height:10.9px}
.closing{top:849px;font-size:9.6px;line-height:13px;color:var(--pink);font-weight:700}

/* right column */
.faq-big{left:810px;top:-9px;font-size:70px;font-weight:700;color:var(--pink-pale)}
.faq-head{left:880px;top:37px;font-size:19.5px;font-weight:300;color:var(--navy)}
.qt{font-family:"Roboto",Arial,sans-serif;font-size:10.5px;line-height:1.08;color:var(--navy)}
.qt strong{color:var(--pink)}
.box{border:1px solid var(--pink)}
.box-blue{border:1px solid var(--navy)}
.small{font-size:7.4px;line-height:10px}
.scale-lbl{font-size:6.4px;color:var(--grey)}
.chart-lbl{top:292px;font-size:7px;color:var(--grey);font-weight:700;text-align:center;line-height:1.1}
.prep{left:821px;top:408px;width:252px}
.prep ul{list-style:disc;padding-left:18px;margin-top:9px}
.time-30{left:1077px;top:538px;font-size:38px;font-weight:700;color:#6a6a6a}
.time-to{left:1108px;top:556px;font-size:11px;color:var(--pink)}
.time-60{left:1125px;top:533px;font-size:50px;font-weight:700;color:var(--pink)}
.time-min{left:1129px;top:579px;font-size:13px;color:var(--pink);font-weight:300}
.cost-head{left:977px;top:723px;font-size:24px;font-weight:300;color:var(--navy)}
.cost-table{left:800px;top:790px;width:400px;border-collapse:collapse;font-size:7.4px}
.cost-table td{padding:0 6px;height:17.3px;line-height:1.1;color:#555}
.cost-table tr.shade td{background:var(--pink-pale)}
.cost-table td:first-child{width:79px;text-align:center}
.cost-table td:last-child{width:52px;font-weight:700}
.band{left:0;top:850px}
</style>
</head>
<body>

<!-- LEFT COLUMN -->
<ul class="abs facts">
  <li>As you already know, <span class="pk">breast health</span> is incredibly important, and breast problems can develop silently for decades before anything can be picked up on a mammogram!</li>
  <li><span class="pk">Every 2 minutes</span> a woman is diagnosed with Breast Cancer.</li>
  <li><span class="pk">Every 13 minutes</span> a woman in the US loses her life to breast cancer.</li>
  <li>More than <span class="pk">250,000 women under 40</span> in the US live with a breast cancer diagnosis.</li>
  <li>About <span class="pk">one in eight women in the U.S.</span> will develop invasive breast cancer during her lifetime.</li>
  <li><span class="pk">Breast cancer is the most common cancer</span> in American women, behind skin cancer, and second-leading cause of cancer death in women, exceeded only by lung cancer.</li>
  <li>An estimated <span class="pk">232,670 new cases</span> of invasive breast cancer will be diagnosed in U.S. women this year.</li>
  <li>Two of three breast <span class="pk">cancers are found in women</span> 55 or older and approximately 1/3 of all breast cancers occur in women under 45.</li>
  <li>Here at <span class="nv">Bright Oak Care Medicine</span>, we don't just deal with problems after they have formed. We pride ourselves on comprehensive, preventive health-care to keep you happy and healthy, and this is why we have developed a comprehensive Breast Health Screening Program <span class="pk">using state-of-the-art Breast Thermography.</span></li>
</ul>

<div class="abs display what-big">What is</div>
<div class="abs display what-sub">Breast Thermography</div>
<div class="abs display what-q">?</div>

<div class="abs intro">
  <p><span class="pk">Breast Thermography</span> is an exciting addition to breast imaging technology that was <span class="bl">approved by the FDA in 1982</span>. It is an additional tool that doctors use to help determine breast cancer risk and can also indicate the risk of other breast conditions. When Breast Thermography is used in combination with other tests, it gives your doctor an improved overall picture of breast health.</p>
  <p>Breast Thermography uses infra-red imaging technology to scan the breast and <span class="pk">produces an incredibly detailed heat map</span>, which can help detect the new blood vessels that grow from tumors, as well as hormonal imbalances, and other breast-health problems.</p>
  <p>Breast thermography provides an additional piece of the puzzle and is not to be used alone. However, when used together with other imaging and lab tests, it will provide your doctor with much more information, giving a more comprehensive picture of your overall breast health.</p>
</div>

<div class="abs risk">
  <span style="color:var(--pink-light)">low risk</span>
  <span class="dot" style="background:#f0c0f4"></span>
  <span class="dot" style="background:#e8a2f0"></span>
  <span class="dot" style="background:#de80ec"></span>
  <span class="dot" style="background:#d45ee8"></span>
  <span class="dot" style="background:#c63ee2"></span>
  <span class="dot" style="background:#b52cdc"></span>
  <span class="dot" style="background:#a21dd6"></span>
  <span class="dot" style="background:#9018cf"></span>
  <span style="color:var(--purple)">high risk</span>
</div>

<div class="abs thermo" style="left:38px;background:radial-gradient(circle at 30% 60%,#c0306a 0 8%,#3fb54a 20%,#3a8fd0 55%,#2a3ab0 85%,#111 100%)" role="img" aria-label="Thermal image of the chest, TH1 normal pattern"></div>
<div class="abs thermo" style="left:153px;background:radial-gradient(circle at 45% 55%,#b0103a 0 10%,#f04020 28%,#f8d030 52%,#49b848 75%,#2a58c0 100%)" role="img" aria-label="Thermal image of the chest, TH5 high heat pattern"></div>
<div class="abs th-code" style="left:111px">TH 1</div>
<div class="abs th-cap" style="left:42px">Normal thermogram</div>
<div class="abs th-code" style="left:153px">TH 5</div>
<div class="abs th-cap" style="left:153px;width:110px">Very high probability of malignant disease</div>

<div class="abs display ben-big">Benefits</div>
<div class="abs display ben-sub">of Breast<br>Thermography</div>
<ul class="abs ben-list">
  <li class="pk">Safe</li>
  <li class="pk">Painless</li>
  <li>No harmful radiation</li>
  <li>Can be used at any age</li>
  <li>No limit on tests per year</li>
  <li>Fast</li>
</ul>

<div class="abs diff">
  <div class="l1">What is the</div>
  <div class="l2">DIFFERENCE</div>
  <div class="l3">between a</div>
  <div class="l4">Mammogram</div>
  <span class="amp">&amp;</span>
  <div class="l5">Breast</div>
  <div class="l6">Thermography</div>
</div>

<div class="abs diff-text">
  <p>Unlike a mammogram, which is used to diagnose breast cancer by using X-Rays that find denser tissues, a Breast Thermography Machine uses Infra-Red Imaging to find "hotter" areas of the breast that are more active.</p>
  <p>A Mammogram is like taking a still photograph that tells you how a breast looks.</p>
  <p>Breast Thermography is like actively looking through a set of infra-red heat goggles that can tell you how the breast is working.</p>
  <p>Both tests give us different information and are both important when it comes to assessing your breast health.</p>
</div>

<!-- MIDDLE COLUMN -->
<div class="abs display who-title"><strong>Who</strong>should have</div>
<div class="abs display who-sub">Breast Thermography</div>
<div class="abs display who-q">?</div>

<div class="abs mid who-list">
  <p>Women with <b>Fibrocystic Breasts</b> or <b>Dense Breasts</b>.</p>
  <p>Dense breast tissue contains more glands and ligaments and less fat.<br>Mammograms have trouble seeing through dense tissue;<br>however thermograms can easily evaluate dense breast tissue.</p>
  <p>Women with <b>inconclusive mammograms.</b></p>
  <p><span class="bl">Thermography can reduce</span> the need for biopsies by up to 20%.</p>
  <p>Women with <b>surgical implants</b>.</p>
  <p>The risk of an implant rupturing during a mammogram is a small, but valid concern.<br>With thermography there is <b>no compression and no risk!</b></p>
  <p>Younger women who want to <span class="pk">limit radiation exposure</span> to the breast.</p>
  <p><b>A routine mammogram</b> consists of two views of each breast<br>and contains up to 0.2 rad per x-ray. Radiation accumulates in breast tissue,<br>and each 1.0 rad of exposure increases the risk of breast cancer by 1 percent.<br>Because thermography images thermal heat emanating from the body,<br><span class="bb">there is no radiation risk whatsoever.</span></p>
  <p>Women with a <span class="pk">family history of breast cancer</span>.</p>
  <p>Annual breast screening is not usually recommended until age 40; however,<br>if you fall into the high risk category, thermograms should be started<br>in the mid 20's in order to obtain a baseline for all future comparisons.</p>
  <p>Women struggling with <b>hormone imbalance</b>.</p>
  <p>Women who want a <b>baseline for overall breast health</b>.</p>
  <p>Women who have had <b>surgical procedures or biopsies</b> <span style="color:var(--pink)">to the breast</span>.</p>
  <p>Women who have had a <span class="bl">mastectomy</span>.</p>
  <p>You have had an <b>abnormal mammogram</b> and have been told<br>you need to wait 6 months before your next mammogram.</p>
  <p class="pk">ANY WOMAN CONCERNED ABOUT BREAST HEALTH.</p>
</div>

<div class="abs display seven">7</div>
<div class="abs mid display addl-big">additional facts about</div>
<div class="abs mid display addl-sub">Breast Thermography</div>
<div class="abs mid display addl-vs">vs. mammograms</div>

<p class="abs mid fact" style="top:564px"><span style="color:var(--pink)">Breast thermography</span> has been <span class="bl">FDA approved</span><br>as an adjunct diagnostic tool to mammograms since 1982.</p>
<p class="abs mid fact" style="top:609px">There have been <b>800 peer-reviewed breast thermography studies</b> in which over a quarter<br>million women have participated in large-scale studies over 12 years.<br>These studies show <span class="bb">thermography to be 90% accurate</span>.</p>
<p class="abs mid fact" style="top:663px">Mammograms in pre-menopausal women can be up to 89% inaccurate, leading to<br>unnecessary procedures, as well as emotional and physical trauma.</p>
<p class="abs mid fact" style="top:707px"><b>Many false negatives occur</b> with mammograms since tumors are frequently located in the<br>upper outer aspects of the breasts where the scans do not reach.</p>
<p class="abs mid fact" style="top:750px">In <b>Europe, Canada, &amp; Australia</b> healthy breasts are routinely screened<br>with thermography. and mammograms are used as a second line of diagnosis.</p>
<p class="abs mid fact" style="top:794px"><b>For earliest</b> <span class="bb">detection</span> <b>and</b> <span style="color:var(--pink)">prevention</span>, it is recommended that women<br>receive baseline breast thermography at age 20,<br>every three years between ages 20-30, and annually from age 30.</p>
<p class="abs mid closing">Starting breast thermography at any age<br>gives you the safest and earliest detection possible.</p>

<!-- RIGHT COLUMN -->
<div class="abs display faq-big">F.A.Q.</div>
<div class="abs display faq-head">Frequently Asked Questions:</div>

<div class="abs qt" style="left:818px;top:70px;width:170px;text-align:right">Can I use <strong>Breast Thermography</strong><br><b>instead</b> of a mammogram<br>to diagnose breast cancer?</div>
<div class="abs box-blue" style="left:992px;top:66px;width:194px;height:94px;border-left:none"></div>
<div class="abs small" style="left:999px;top:72px;width:181px;text-align:justify">No. When it comes to a breast cancer diagnosis, a breast biopsy is the gold-standard for diagnosing breast cancer.<br><br><span class="pk">Breast Thermography</span> is used together with other tests including mammograms, ultrasounds, MRI's, blood testing, and genetic testing, in order to add incredible amounts of detail to generate a comprehensive picture of your breast health and your risk of breast cancer.</div>

<div class="abs box" style="left:813px;top:130px;width:180px;height:70px;border-top:none;border-right:none"></div>
<div class="abs small" style="left:819px;top:134px;width:172px;text-align:justify">By the time a tumor reaches the size of a pin head (approximately two years into its growth) it can no longer be sustained by the normal blood supply and so it develops its own. The development of that blood supply is called angiogenesis. <span class="pk">Thermography is the only technology in place that can detect angiogenesis.</span></div>
<div class="abs qt" style="left:999px;top:166px">Thermography?<br><strong>Mammograms?</strong><br><b>Or both?</b></div>

<svg class="abs" style="left:836px;top:200px" width="364" height="84" viewBox="0 0 364 84" aria-hidden="true">
  <circle cx="11" cy="38" r="4" fill="var(--pink)"/>
  <circle cx="34" cy="38" r="4" fill="var(--pink)"/>
  <circle cx="58" cy="38" r="8.5" fill="var(--sky)"/>
  <circle cx="92" cy="38" r="17.5" fill="var(--sky)"/>
  <circle cx="144" cy="38" r="25.5" fill="var(--green)"/>
  <circle cx="216" cy="38" r="34" fill="var(--green)"/>
  <circle cx="294" cy="38" r="34" fill="var(--purple)"/>
  <rect x="2" y="80" width="110" height="2" fill="#e4e4e4"/>
  <rect x="112" y="80" width="140" height="2" fill="#b0b0b0"/>
  <rect x="252" y="80" width="60" height="2" fill="#9a9a9a"/>
  <rect x="312" y="80" width="52" height="2" fill="#6a6a6a"/>
</svg>
<div class="abs scale-lbl" style="left:838px;top:271px">*sizes to scale 1:1</div>
<div class="abs chart-lbl" style="left:830px;width:54px">Infrared<br>Thermography<br>2mm</div>
<div class="abs chart-lbl" style="left:890px;width:54px">Screening<br>MRI<br>4 - 8mm</div>
<div class="abs chart-lbl" style="left:960px;width:110px">X-Ray Mammogram<br>12 - 16mm</div>
<div class="abs chart-lbl" style="left:1100px;width:62px">Breast<br>Examination<br>20mm</div>

<div class="abs small" style="left:813px;top:321px;width:378px"><span class="bl">Mammogram is not early detection.</span> A cancerous tumor has been growing eight to ten years before it is big enough and dense enough to be detected by mammography. That is why the treatment at that stage is so drastic – removal of breast, underlying muscle, lymph nodes, chemotherapy, radiation therapy and hormonal therapy.</div>

<div class="abs qt" style="left:843px;top:359px;width:119px;text-align:right;font-size:10px">What are the<br><b>side effects</b> of<br><strong>Breast Thermography?</strong></div>
<div class="abs box-blue" style="left:970px;top:361px;width:188px;height:33px;border-right:none"></div>
<div class="abs small" style="left:977px;top:366px;width:180px">There are <b>no known short or long-term side effects</b> of breast thermography. <span class="pk">It is incredibly safe!</span></div>

<div class="abs box" style="left:813px;top:401px;width:330px;height:238px;border-right:none;border-bottom:none"></div>
<div class="abs small prep">
  Prior to the test, please adhere to the following:
  <ul>
    <li><span class="bb">No natural or artificial tanning</span> 5 days prior to your test date.</li>
    <li><span class="pk">No breast manipulation prior to the test</span>, including breast self-exams, compression of the breasts, breast stimulation, breast ultrasound, or mammogram for 24h prior to the test.</li>
    <li><b>No fevers</b> for at least 36h prior to the test.</li>
    <li><b>No steam rooms</b>, saunas, heat packs, or cold packs for at least 4 hours prior to the test.</li>
    <li><b>Do not shave</b> your underarms or use skin creams, lotions, deodorants, or powders on your breast before your test.</li>
    <li><b>No coffee, tea, or tobacco</b> two hours before the test</li>
    <li class="pk">No restrictive clothing</li>
  </ul>
  <p style="margin-top:10px">At the clinic:</p>
  <p style="margin-top:11px;text-align:justify"><span class="bb">Arrive a few minutes early</span> to your appointment. Your body will take time to adjust to the temperature of the clinic. You will be disrobing down to your underwear of choice. <span class="pk">You will meet your thermographer</span> who will explain and demonstrate the required views and positions necessary for your exam. Thermal images are then taken of either the whole body or just the regions of interest. A cold "stress" test is performed with this test, which simply involves placing a hand or foot in a cool bowl of water.</p>
</div>

<div class="abs qt" style="left:1077px;top:406px"><b>How should I<br>prepare</b> for my<br><strong>Breast Thermography</strong><br>appointment?</div>

<div class="abs box-blue" style="left:1074px;top:504px;width:113px;height:92px;border-left:none;border-top:none"></div>
<div class="abs qt" style="left:1077px;top:511px"><b>How long</b> will<br><strong>my appointment</strong><br>last?</div>
<div class="abs display time-30">30</div>
<div class="abs display time-to">to</div>
<div class="abs display time-60">60</div>
<div class="abs display time-min">minutes</div>

<div class="abs box" style="left:1089px;top:609px;width:98px;height:110px;border-left:none;border-top:none"></div>
<div class="abs" style="left:813px;top:716px;width:280px;border-top:1px solid var(--pink)"></div>
<div class="abs qt" style="left:1088px;top:613px;width:90px;text-align:right"><b>When</b><br>will I get<br><strong>my results?</strong></div>

<div class="abs small" style="left:813px;top:649px;width:370px"><b>Our board certified Physician</b> evaluates each thermographic image and creates a report. <span class="bb">Your comprehensive interpretive report</span>, including images, will be ready to follow up within a <b>7-14 Business days</b>.</div>
<div class="abs small" style="left:813px;top:680px;width:378px">Our goal is to educate the community to consider thermography when it comes to their health. Some patients ask us to perform a yearly analysis to identify any changes or possible areas of concern. We understand medical testing can be cause of anxiety. <span class="bb">We aim to make you experience as pleasant and comfortable as possible.</span></div>

<div class="abs display cost-head">Cost</div>
<div class="abs small" style="left:880px;top:749px;width:312px">Thermography is not yet paid by insurance companies. For this reason, we consider this an alternative service, not requiring a doctor's order and payable at the time of service. Current rates are as follows:</div>

<table class="abs cost-table">
  <tr class="shade"><td>THBRA</td><td><b style="color:#333">Thermogram Breast, ANNUAL</b></td><td>$200</td></tr>
  <tr><td>THR01</td><td>Thermogram 1 Region of Interest<br>(Head, Abdomen, Lower extremities, Upper extremities)</td><td>$180</td></tr>
  <tr class="shade"><td>THROB</td><td>Thermogram 1 Region of Interest With Breasts</td><td>$250</td></tr>
  <tr><td>THMHS</td><td>Men's Screen<br>(includes, head, neck, thyroid, chest, abdomen, upper and lower back)</td><td>$275</td></tr>
  <tr class="shade"><td>THWHS</td><td>Women's Screen<br>(includes head, neck, thyroid, breast, abdomen/pelvis, upper and lower back)</td><td>$325</td></tr>
  <tr><td>THPS</td><td>Thermogram Cervical or Lumbar Study, 3 Sets of images</td><td>$350</td></tr>
</table>

<!-- bottom band -->
<svg class="abs band" width="1200" height="77" viewBox="0 0 1200 77" aria-hidden="true">
  <path d="M0 8 L560 26 L800 40 L1200 42 L1200 77 L0 77 Z" fill="var(--magenta)" opacity=".55"/>
  <path d="M0 34 L600 40 L800 45 L1200 50 L1200 77 L0 77 Z" fill="var(--magenta)"/>
</svg>

</body>
</html>
```